chiptune chip tuning car tuning company need a banner as advertising

we need a professional banner for outdoor advertising. please as vector.

we are a chip tuning company in germany.

what should be on it:
Chip tuning from € 299

More performance, less consumption

01765048837
www.mavolt.de

CHIPTUNING - Eco-Optimization - AGR / DPF SERVICE - KEB certificate - SOFTWARE DEVELOPMENT - File service
-------------------------------------------------- ------------------------------------------
in German:

we need a banner for outdoor advertising. please as vector.

what should be on it:

Chip tuning from € 299

Telephone number: 01765048837
www.mavolt.de

```html
<!DOCTYPE html>
<html lang="en">
<head>
<meta charset="utf-8">
<title>MAVOLT – Chip tuning banner</title>
<link rel="stylesheet" href="https://fonts.googleapis.com/css2?family=Marcellus&family=Montserrat:wght@500;600;700&family=Open+Sans:wght@400;600&display=swap">
<style>
  :root {
    --stage: #e6e6e6;
    --banner-bg: #212121;
    --gold: #fbd795;
    --gold-band: #fbd898;
    --gold-deep: #c9962e;
    --white: #ffffff;
  }
  * { margin: 0; padding: 0; box-sizing: border-box; }
  html, body {
    width: 1200px;
    height: 1065px;
    overflow: hidden;
    background: var(--stage);
  }
  .banner {
    position: absolute;
    left: 0;
    top: 190px;
    width: 1200px;
    height: 686px;
    background: var(--banner-bg);
    overflow: hidden;
  }
  .brand {
    position: absolute;
    left: 700px;
    top: 44px;
    display: flex;
    align-items: center;
    gap: 16px;
    font-family: "Montserrat", sans-serif;
    font-weight: 700;
    font-size: 58px;
    letter-spacing: 4px;
    color: var(--gold);
    line-height: 1;
  }
  .brand-mark {
    width: 44px;
    height: 44px;
    background: var(--gold);
  }
  .headline {
    position: absolute;
    left: 0;
    width: 640px;
    top: 96px;
    text-align: center;
    font-family: "Marcellus", serif;
    font-size: 52px;
    line-height: 56px;
    color: var(--gold);
  }
  .offer {
    position: absolute;
    left: 126px;
    top: 259px;
    width: 386px;
    height: 144px;
    border: 2px solid var(--gold);
  }
  .offer-title {
    position: absolute;
    left: 49px;
    top: 8px;
    font-family: "Montserrat", sans-serif;
    font-weight: 600;
    font-size: 43px;
    color: var(--gold);
    line-height: 1;
  }
  .offer-from {
    position: absolute;
    left: 49px;
    top: 60px;
    font-family: "Montserrat", sans-serif;
    font-weight: 500;
    font-size: 29px;
    color: var(--gold);
    line-height: 1;
  }
  .offer-price {
    position: absolute;
    left: 148px;
    top: 50px;
    font-family: "Open Sans", sans-serif;
    font-weight: 600;
    font-size: 76px;
    letter-spacing: -2px;
    color: var(--white);
    line-height: 1;
  }
  .services {
    position: absolute;
    left: 57px;
    top: 460px;
    list-style: none;
    font-family: "Montserrat", sans-serif;
    font-weight: 500;
    font-size: 27px;
    line-height: 40.5px;
    color: var(--white);
  }
  .car-illustration {
    position: absolute;
    left: 582px;
    top: 202px;
    width: 578px;
    height: 277px;
  }
  .contact {
    position: absolute;
    left: 876px;
    top: 478px;
    font-family: "Open Sans", sans-serif;
    font-size: 32px;
    color: var(--white);
    line-height: 43px;
    list-style: none;
  }
  .contact li {
    display: flex;
    align-items: center;
    gap: 26px;
  }
  .contact svg { width: 30px; height: 30px; flex: none; }
  .band {
    position: absolute;
    left: 0;
    bottom: 0;
    width: 100%;
    height: 37px;
    background: var(--gold-band);
  }
</style>
</head>
<body>
  <main class="banner">
    <div class="brand"><span class="brand-mark"></span>MAVOLT</div>

    <h1 class="headline">MORE PERFORMANCE,<br>LESS CONSUMPTION</h1>

    <div class="offer">
      <p class="offer-title">Chip tuning</p>
      <p class="offer-from">from</p>
      <p class="offer-price">€ 299</p>
    </div>

    <ul class="services">
      <li>CHIPTUNING - Eco-Optimization</li>
      <li>AGR / DPF SERVICE - KEB certificate</li>
      <li>SOFTWARE DEVELOPMENT - File service</li>
    </ul>

    <svg class="car-illustration" role="img" aria-label="Gold illustration of a sports car speeding with motion streaks" viewBox="0 0 578 277">
      <defs>
        <linearGradient id="car-gold" x1="0" y1="0" x2="1" y2="1">
          <stop offset="0" stop-color="#fbd795"/>
          <stop offset="1" stop-color="#c9962e"/>
        </linearGradient>
      </defs>
      <rect width="578" height="277" rx="16" fill="url(#car-gold)" opacity="0.85"/>
    </svg>

    <ul class="contact">
      <li>
        <svg viewBox="0 0 30 30" aria-hidden="true">
          <rect x="9" y="3" width="12" height="24" rx="2" fill="none" stroke="#fbd795" stroke-width="2"/>
          <circle cx="15" cy="23.5" r="1.2" fill="#fbd795"/>
        </svg>
        <span>0176 5048837</span>
      </li>
      <li>
        <svg viewBox="0 0 30 30" aria-hidden="true">
          <g fill="none" stroke="#fbd795" stroke-width="1.8">
            <circle cx="15" cy="15" r="12"/>
            <ellipse cx="15" cy="15" rx="5.5" ry="12"/>
            <line x1="3" y1="15" x2="27" y2="15"/>
            <path d="M5 9h20M5 21h20"/>
          </g>
        </svg>
        <span>www.mavolt.de</span>
      </li>
    </ul>

    <div class="band"></div>
  </main>
</body>
</html>
```